Korvale Power Solutions Business Card

We are based in Columbus, Ohio and need a business card that represents our modern approach to energy projects. We perform energy projects for buildings that include Heating/Cooling Controls, Mechanical Equipment, LED Lighting, Envelope Improvements, etc. We have saved clients up to 65% of their total energy costs. Our logo is attached. We like designs that integrate our logo into one side and then provide contact/person info on the other. We would like to limit the number of colors to keep printing costs down. We want to maintain the blue/green in our logo.

```html
<!DOCTYPE html>
<html lang="en">
<head>
<meta charset="utf-8">
<title>Korvale Power Solutions – Business Card</title>
<link rel="stylesheet" href="https://fonts.googleapis.com/css2?family=Questrial&display=swap">
<style>
  :root {
    --brand-blue: #2f7fc1;
    --brand-green: #7dc242;
    --ink: #4a4f55;
    --paper: #ffffff;
    --backdrop: #ecebe8;
  }
  * { box-sizing: border-box; margin: 0; padding: 0; }
  html, body {
    width: 710px; height: 1200px; overflow: hidden;
    background: var(--backdrop);
    font-family: "Questrial", "Century Gothic", sans-serif;
    color: var(--ink);
  }
  .canvas { position: relative; width: 710px; height: 1200px; }
  .card {
    position: absolute; left: 55px; width: 600px; height: 343px;
    background: var(--paper); overflow: hidden;
    box-shadow: 0 6px 18px rgba(0,0,0,.18);
  }
  .card--front { top: 170px; }
  .card--back { top: 690px; }
  .card-bands { position: absolute; inset: 0; }
  .brand-seal {
    position: absolute; border-radius: 50%;
    background: var(--paper);
    border: 10px solid var(--brand-blue);
    display: flex; align-items: center; justify-content: center;
    text-align: center; color: var(--brand-blue);
    line-height: 1.15; letter-spacing: .5px;
  }
  .card--front .brand-seal { left: 125px; top: 92px; width: 160px; height: 160px; font-size: 17px; }
  .card--back .brand-seal { left: 70px; top: 35px; width: 210px; height: 210px; font-size: 22px; }
  .person { position: absolute; left: 320px; top: 62px; }
  .person-name { font-size: 22px; letter-spacing: 1.5px; text-transform: uppercase; color: var(--ink); }
  .person-title { font-size: 13px; color: var(--brand-blue); margin-top: 4px; }
  .contact-list { position: absolute; left: 320px; top: 140px; list-style: none; font-size: 12.5px; }
  .contact-list li { display: flex; align-items: flex-start; gap: 10px; margin-bottom: 11px; line-height: 1.35; }
  .contact-icon { width: 16px; height: 16px; flex: none; margin-top: 1px; }
  .back-web {
    position: absolute; left: 0; right: 0; bottom: 28px;
    text-align: center; color: var(--paper); font-size: 16px; letter-spacing: 3px;
  }
</style>
</head>
<body>
<main class="canvas">

  <section class="card card--front" aria-label="Card front">
    <svg class="card-bands" viewBox="0 0 600 343" aria-hidden="true">
      <rect x="0" y="0" width="24" height="343" fill="var(--brand-blue)"/>
      <rect x="24" y="0" width="180" height="343" fill="var(--brand-green)"/>
    </svg>
    <div class="brand-seal">Korvale<br>Power<br>Solutions</div>
    <div class="person">
      <p class="person-name">Dale Whitcomb</p>
      <p class="person-title">President</p>
    </div>
    <ul class="contact-list">
      <li>
        <svg class="contact-icon" viewBox="0 0 16 16"><rect width="16" height="16" fill="var(--brand-blue)"/><path d="M5 3.5h2l1 2.5-1.3 1a6 6 0 0 0 2.3 2.3l1-1.3 2.5 1v2c0 .6-.5 1-1 1A8 8 0 0 1 4 4.5c0-.5.4-1 1-1z" fill="#fff"/></svg>
        <span>P 614.555.0182<br>F 614.555.0190</span>
      </li>
      <li>
        <svg class="contact-icon" viewBox="0 0 16 16"><rect width="16" height="16" fill="var(--brand-green)"/><rect x="3" y="4.5" width="10" height="7" fill="none" stroke="#fff" stroke-width="1.2"/><path d="M3 4.5l5 4 5-4" fill="none" stroke="#fff" stroke-width="1.2"/></svg>
        <span>dale@korvalepower.com</span>
      </li>
      <li>
        <svg class="contact-icon" viewBox="0 0 16 16"><rect width="16" height="16" fill="var(--brand-blue)"/><circle cx="8" cy="8" r="4.5" fill="none" stroke="#fff" stroke-width="1.2"/><path d="M3.5 8h9M8 3.5c-2 2.5-2 6.5 0 9M8 3.5c2 2.5 2 6.5 0 9" fill="none" stroke="#fff" stroke-width="1"/></svg>
        <span>www.korvalepower.com</span>
      </li>
      <li>
        <svg class="contact-icon" viewBox="0 0 16 16"><rect width="16" height="16" fill="var(--brand-green)"/><path d="M8 13s-4-4-4-6.5a4 4 0 0 1 8 0C12 9 8 13 8 13z" fill="#fff"/><circle cx="8" cy="6.5" r="1.4" fill="var(--brand-green)"/></svg>
        <span>480 Harlow Avenue, Suite 210<br>Columbus, OH 43215</span>
      </li>
    </ul>
  </section>

  <section class="card card--back" aria-label="Card back">
    <svg class="card-bands" viewBox="0 0 600 343" aria-hidden="true">
      <rect x="330" y="0" width="270" height="262" fill="var(--brand-green)"/>
      <rect x="0" y="262" width="600" height="81" fill="var(--brand-blue)"/>
    </svg>
    <div class="brand-seal">Korvale<br>Power<br>Solutions</div>
    <p class="back-web">www.korvalepower.com</p>
  </section>

</main>
</body>
</html>
```